Business Card Design Project for a Restaurant/Wine Bar

New, fresh business card design for Verdano Wine Bar & Restaurant, Selvane Harbor, Westmark. We are an established restaurant on the Oregon coast featuring "Italian coastal cuisine."

"Verdano" means bay leaf in Italian. We aren't sure if we would like our logo on the card or not, but if you have something interesting that uses it, then please do so. The basic information is essential - full restaurant name, address, phone and website (do not use www). The font on our menu and wine list may give you some sort of an idea of our style.

One-sided card needed as we often use the backside to write down various types of info for customers.

After seeing a few submissions, we would like to see what designers can come up with-using the logo, just the leaf, or none at all. Sky is the limit as long as our full restaurant name, address, phone and website (please leave out www) are there. Please contact us if questions!

I appreciate all of your designs! Our deadline is next week, but I will continue to give feedback on designs as I can. This is our busiest season, so my co-owner/chef/husband, won't have time to look at the designs for awhile. When he does, we can make our decision.

cheers,
Mirel

Target Market(s)

Fine dining/wine crowd. Would like something simple and elegant, but not pretentious or stuffy. Verdano means bay laurel (bay leaf) in Italian (please see our logo).

Industry/Entity Type

Restaurant

Requirements
Must have
• Full Name of Restaurant: Verdano Wine Bar & Restaurant
Address: 812 Fenwick Ave NW, Selvane Harbor, Westmark 97538
Phone: 541.555.0193
website: verdanowinebar.example (do not use www)
Should not have
• Loud colors.

```html
<!DOCTYPE html>
<html lang="en">
<head>
<meta charset="utf-8">
<title>Verdano Wine Bar &amp; Restaurant — Business Card</title>
<link href="https://fonts.googleapis.com/css2?family=Lato:wght@400;700;900&family=Italianno&display=swap" rel="stylesheet">
<style>
  :root {
    --brown: #4a3322;
    --cream: #ffffff;
    --gold: #f1d66a;
    --map-light: #eef1f3;
    --map-tone: #d9e3ea;
    --edge: #bdb8b2;
  }
  html, body {
    margin: 0;
    padding: 0;
    overflow: hidden;
    background: var(--cream);
  }
  .card {
    position: relative;
    width: 699px;
    height: 1200px;
    background: var(--brown);
    overflow: hidden;
    box-shadow: inset 0 0 0 2px var(--edge);
    font-family: "Lato", Arial, sans-serif;
    color: var(--cream);
  }
  .card__panel {
    position: absolute;
    inset: 0;
  }
  .name {
    position: absolute;
    left: 40px;
    top: 72px;
    margin: 0;
    line-height: 1;
  }
  .name__main {
    display: block;
    font-size: 60px;
    font-weight: 700;
    letter-spacing: 3px;
  }
  .name__sub {
    display: block;
    font-size: 42px;
    font-weight: 400;
    letter-spacing: 3px;
    margin-top: 8px;
  }
  .tagline {
    position: absolute;
    left: 40px;
    top: 372px;
    margin: 0;
    font-family: "Italianno", cursive;
    font-size: 66px;
    color: var(--gold);
    font-weight: 400;
  }
  .owner {
    position: absolute;
    right: 354px;
    top: 522px;
    margin: 0;
    text-align: right;
    font-size: 34px;
    line-height: 1.3;
    letter-spacing: 1px;
  }
  .owner__role {
    display: block;
    font-weight: 700;
    letter-spacing: 3px;
  }
  .address {
    position: absolute;
    right: 44px;
    top: 112px;
    margin: 0;
    writing-mode: vertical-lr;
    font-style: normal;
    font-weight: 700;
    font-size: 36px;
    line-height: 1.35;
    color: var(--brown);
  }
  .map {
    position: absolute;
    left: 404px;
    top: 680px;
    width: 282px;
    height: 330px;
    border-radius: 6px;
    background: linear-gradient(160deg, var(--map-light), var(--map-tone));
  }
  .contact {
    position: absolute;
    left: 40px;
    bottom: 62px;
    margin: 0;
    font-style: normal;
  }
  .contact__phone {
    display: block;
    font-size: 52px;
    letter-spacing: 1px;
  }
  .contact__web {
    display: block;
    font-size: 30px;
    margin-top: 14px;
  }
</style>
</head>
<body>
  <main class="card">
    <svg class="card__panel" width="699" height="1200" viewBox="0 0 699 1200" aria-hidden="true">
      <path fill="var(--cream)" d="M508 0 L699 0 L699 1160 C620 1110 420 1085 396 1010 C376 940 372 760 386 690 C402 610 508 570 508 470 Z"/>
    </svg>

    <h1 class="name">
      <span class="name__main">VERDANO</span>
      <span class="name__sub">WINE BAR &amp;</span>
      <span class="name__sub">RESTAURANT</span>
    </h1>

    <p class="tagline">Italian Coastal Cuisine</p>

    <p class="owner">Mirel Halvorsen<span class="owner__role">OWNER</span></p>

    <address class="address">812 Fenwick Ave NW<br>Selvane Harbor, Westmark 97538</address>

    <div class="map" role="img" aria-label="Small street map showing the restaurant location near the river and highway"></div>

    <address class="contact">
      <span class="contact__phone">541.555.0193</span>
      <span class="contact__web">verdanowinebar.example</span>
    </address>
  </main>
</body>
</html>
```